Postcard Design

We are a landscape maintenance, design and build company. Our services include weekly property maintenance, spring and fall clean ups, tree, shrub and plant care, pool renovations and new installations, patio and retaining wall design and construction, deign and building of outdoor kitchens, fireplaces and water features.we are a fully insured NJ Home Improvement Contractor License 27KP81926058

It Company

```html
<!DOCTYPE html>
<html lang="en">
<head>
<meta charset="utf-8">
<title>R&amp;T Outdoor Works Postcard</title>
<link href="https://fonts.googleapis.com/css2?family=Roboto+Condensed:wght@700&family=Lato:ital,wght@0,400;0,700;1,400;1,700&display=swap" rel="stylesheet">
<style>
:root{
  --page:#ececec;
  --green:#1f8a3c;
  --green-dark:#156b2c;
  --green-light:#3db34f;
  --charcoal:#2e2e2e;
  --charcoal-light:#4a4a4a;
  --paper:#ffffff;
  --mist:#e9e9e9;
  --ink:#2b2b2b;
  --stamp:#d9d9dc;
}
*{margin:0;padding:0;box-sizing:border-box}
html,body{width:825px;height:1200px;overflow:hidden}
body{background:var(--page);position:relative;font-family:"Lato",sans-serif}
.card{position:absolute;left:115px;width:597px;height:462px;background:var(--paper);box-shadow:0 6px 14px rgba(0,0,0,.28);overflow:hidden}
.card--front{top:100px}
.card--back{top:638px}
.card svg.shapes{position:absolute;left:0;top:0;width:597px;height:462px}
.t{position:absolute;white-space:nowrap}
.display{font-family:"Roboto Condensed",sans-serif;font-weight:700}
.headline{left:25px;top:20px;font-size:28px;color:#fff;letter-spacing:-.3px}
.subline{left:26px;top:50px;font-size:16.5px;color:#fff}
.license{left:26px;top:117px;font-size:21px;color:var(--ink)}
.hours{left:26px;top:143px;font-size:20px;color:var(--green-light)}
.brand-name{left:26px;top:206px;font-size:25px;color:var(--green-light)}
.call{left:26px;top:239px;font-size:21px;color:#fff;font-weight:700}
.brand-block{position:absolute;left:0;top:285px;width:155px;height:127px;text-align:center}
.brand-block .mark{display:block;width:22px;height:22px;border-radius:50%;background:var(--green-dark);margin:18px auto 8px}
.brand-block .brand-word{font-family:"Roboto Condensed",sans-serif;font-weight:700;font-size:18px;color:var(--green-dark);line-height:1}
.brand-block .tagline{font-size:8px;font-weight:700;color:var(--ink);margin-top:6px}
.brand-block .phone{font-size:10px;font-weight:700;color:var(--ink);margin-top:2px}
.services-title{left:181px;top:300px;font-size:15.5px;color:#fff}
.services{position:absolute;top:332px;list-style:none;color:#fff;font-size:10.5px;font-style:italic;line-height:13.7px}
.services li{position:relative;padding-left:11px}
.services li::before{content:"";position:absolute;left:1px;top:5px;width:4px;height:4px;border-radius:50%;background:#fff}
.services li.cont::before{display:none}
.services--a{left:182px}
.services--b{left:344px}
.address{left:14px;top:434px;font-size:11px;font-style:italic;color:#fff;letter-spacing:.5px}
.web-line{left:223px;top:434px;font-size:11px;font-style:italic;color:#ddd;letter-spacing:.5px}
.back-headline{left:28px;top:181px;font-size:25px;color:var(--green)}
.back-subline{left:28px;top:210px;font-size:16px;color:var(--ink)}
.back-license{left:27px;top:256px;font-size:21px;color:#fff}
.back-call{left:33px;top:317px;font-size:17px;color:#fff;font-weight:700}
.back-web{left:72px;top:343px;font-size:11px;color:#fff;font-style:italic;font-weight:700}
</style>
</head>
<body>

<section class="card card--front">
  <svg class="shapes" viewBox="0 0 597 462">
    <defs>
      <linearGradient id="mistGrad" x1="0" x2="1"><stop offset="0" stop-color="#ffffff"/><stop offset="1" stop-color="#d6d6d6"/></linearGradient>
      <linearGradient id="greenGrad" x1="0" x2="1"><stop offset="0" stop-color="#1a7a33"/><stop offset="1" stop-color="#2a9a45"/></linearGradient>
      <linearGradient id="darkGrad" x1="0" y1="0" x2="0" y2="1"><stop offset="0" stop-color="#555"/><stop offset="1" stop-color="#262626"/></linearGradient>
      <linearGradient id="patioGrad" x1="0" y1="0" x2="1" y2="1"><stop offset="0" stop-color="#2f5e9c"/><stop offset=".35" stop-color="#a07060"/><stop offset=".7" stop-color="#8a6450"/><stop offset="1" stop-color="#4d6b2e"/></linearGradient>
    </defs>
    <rect width="597" height="462" fill="#f0f0f0"/>
    <polygon points="0,0 355,0 318,58 308,56 300,90 0,90" fill="url(#greenGrad)"/>
    <polygon points="0,94 302,94 262,190 0,190" fill="url(#mistGrad)"/>
    <polygon points="355,0 597,0 597,210 262,210" fill="#fff"/>
    <polygon points="362,0 597,0 597,206 270,206" fill="url(#patioGrad)" role="img" aria-label="Photo of a paved patio beside a swimming pool with palms and planting"/>
    <rect x="155" y="215" width="442" height="200" fill="url(#greenGrad)"/>
    <polygon points="0,192 358,192 346,282 0,282" fill="url(#darkGrad)"/>
    <rect x="0" y="285" width="155" height="127" fill="url(#mistGrad)"/>
    <circle cx="415" cy="238" r="36" fill="#6f8a8f" stroke="#fff" stroke-width="5" role="img" aria-label="Photo of a stone wall beside a pool"/>
    <circle cx="530" cy="238" r="40" fill="#6f8a5a" stroke="#fff" stroke-width="5" role="img" aria-label="Photo of a paved driveway lined with shrubs"/>
    <rect x="0" y="420" width="597" height="42" fill="url(#darkGrad)"/>
    <polygon points="0,420 198,420 212,462 0,462" fill="url(#greenGrad)"/>
    <polygon points="198,420 203,420 217,462 212,462" fill="#fff"/>
  </svg>

  <h1 class="t display headline">We are a fully insured</h1>
  <p class="t display subline">NJ Home Improvement Contractor</p>
  <p class="t license">License 27KP81926058</p>
  <p class="t hours">Open 24 Hours</p>
  <p class="t display brand-name">R&amp;T Outdoor Works</p>
  <p class="t call">Call us at +44 7700 900123</p>

  <div class="brand-block">
    <span class="mark"></span>
    <div class="brand-word">R&amp;T OUTDOOR WORKS</div>
    <div class="tagline">Landscaping - Snow Removal</div>
    <div class="phone">555-014-2290</div>
  </div>

  <h2 class="t display services-title">We are landscape maintenance, design and build company</h2>
  <ul class="services services--a">
    <li>Weekly property</li>
    <li class="cont">maintenance</li>
    <li>Spring and fall clean ups</li>
    <li class="cont">Tree, shrub and plant care</li>
  </ul>
  <ul class="services services--b">
    <li>Pool renovations &amp; new installations</li>
    <li>Patio and retaining wall design &amp; construction,</li>
    <li>Deign and building of outdoor kitchens</li>
    <li>Fireplaces and water features</li>
  </ul>

  <p class="t address">12 Mill Lane , Ashford</p>
  <p class="t web-line">Please visit us to know more about us at: www.rtoutdoorworks.com</p>
</section>

<section class="card card--back">
  <svg class="shapes" viewBox="0 0 597 462">
    <defs>
      <linearGradient id="gardenGrad" x1="0" y1="0" x2="1" y2="1"><stop offset="0" stop-color="#8d9a8a"/><stop offset=".5" stop-color="#5f7a3e"/><stop offset="1" stop-color="#c9c5b8"/></linearGradient>
      <linearGradient id="greenGradB" x1="0" x2="1"><stop offset="0" stop-color="#1a7a33"/><stop offset="1" stop-color="#2a9a45"/></linearGradient>
      <linearGradient id="darkGradB" x1="0" y1="0" x2="0" y2="1"><stop offset="0" stop-color="#555"/><stop offset="1" stop-color="#262626"/></linearGradient>
      <linearGradient id="mistGradB" x1="0" x2="1"><stop offset="0" stop-color="#ffffff"/><stop offset="1" stop-color="#dcdcdc"/></linearGradient>
    </defs>
    <rect x="0" y="140" width="290" height="104" fill="url(#mistGradB)"/>
    <polygon points="0,0 283,0 283,140 145,162 0,140" fill="url(#gardenGrad)" role="img" aria-label="Photo of a paved garden with young trees and planting bed"/>
    <polyline points="0,146 145,168 283,146" fill="none" stroke="var(--green)" stroke-width="6"/>
    <rect x="284" y="0" width="6" height="244" fill="var(--green)"/>
    <polygon points="290,232 308,244 290,244" fill="#bdbdbd"/>
    <polygon points="0,247 310,247 297,294 0,294" fill="url(#darkGradB)"/>
    <rect x="0" y="300" width="290" height="74" fill="url(#greenGradB)"/>
    <rect x="476" y="44" width="78" height="74" fill="var(--stamp)"/>
  </svg>

  <p class="t display back-headline">We are a fully insured</p>
  <p class="t display back-subline">NJ Home Improvement Contractor</p>
  <p class="t back-license">License 27KP81926058</p>
  <p class="t back-call">Call us at +44 7700 900123</p>
  <p class="t back-web">www.rtoutdoorworks.com</p>
</section>

</body>
</html>
```